Quiet Horizon Splash page

We want a page to educate the facility managers of Office buildings on the wasted lighting that is left on at night time in their buildings. The page should encourage them to reach out to us for ways to reduce/eliminate the wasted lighting.
Part of the motivation is created by showing photographs of city skylines, and highlight specific buildings, and floors in buildings that have lights left on when the light is not needed. We have attached photos of the San Francisco and LA skylines. We have also created a page with youtube videos educating on light pollution. http://www.velotransit-example.com/education-center-2/velotransit-video-library/
Details:
- We would like a graphic on the page that is the symbol to represent the Quiet Horizon we are working to create.
- The page should be able to segment different cities
- The page should be stand alone with enough information to be valuable, but also should link into more details
- The page should tie into our existing site www.velotransit-example.com
- The page should motivate people to eliminate their wasted light by contacting us
Updates

Hi all, We have received a number of designs, and some are close to our expectation. We will choose a 1st and 2nd place tomorrow night. Here is more clarification based on the designs being submitted: (Please edit your submission if it does not match with the notes below) 1. This design is Not for a homepage or to represent VeloTransit corporately. This design is only to do an interior page that will be the Quiet Horizon initiative. 2. The "Symbol to represent the Quiet Horizon" is a graphic, logo or image that can universally be recognized as representing our Quiet Horizon initiative. This would be used on the webpage and literature we may develop in the future. 3. We expect people visiting this Quiet Horizon page to ask a couple questions. * "What is the Quiet Horizon?" * Is my building causing the wasted lighting (Can I look at a photo of my city {San Francisco, Los Angeles, New York City} and see my building lit up at night? * Is VeloTransit creating a Quiet Horizon? (See images from every 6 months of the same city skyline to see how it is changing) 4. The webpage should not focus on the specific capabilities, skills, tools or software of VeloTransit. It should only focus on the Who, What, Where, Why, How of creating a Quiet Horizon.

Here are notes to help with the design: - Use our uploaded skyline images. - Highlight a level of light left on in those images. and note, "Is your lighting wasted for hours every night?" - Highlight a dark area of a building in those images and note "We helped create a Quiet Horizon here!" - Add an email address to contact us at the bottom and say, "I want to be part of the Quiet Horizon in my city!""

Hi All Designers, Sorry for the delay while I was traveling the past week. We had 62 designs submitted and we have narrowed it down to 7. We are voting this week on designs that are best and then we will choose First place and Second place awards. Thanks! Peter

Target Market(s)

Owners and managers of large office buildings in Western speaking countries. Generally adult male aged 30-60.

Industry/Entity Type

Education

Requirements
Must have
• Sectioned areas for different cities based on where the person is visiting our website from. Major cities we focus on include: Los Angeles, San Francisco, New York City, Philadelphia
Nice to have
• Graphic or image logo representing the Quiet Horizon.
Should not have
• Do not focus on VeloTransit. Focus on the Quiet Horizon initiative.

```html
<!DOCTYPE html>
<html lang="en">
<head>
<meta charset="utf-8">
<title>Quiet Horizon</title>
<link rel="stylesheet" href="https://fonts.googleapis.com/css2?family=Open+Sans:wght@300;400;600;700&display=swap">
<style>
:root{
  --green:#5cb04f;
  --green-dark:#3f8f36;
  --green-band:#6dbd63;
  --orange:#f26a21;
  --orange-light:#f99a3d;
  --ink:#2b2b2b;
  --muted:#8a8a8a;
  --soft-bg:#f1f1f1;
  --white:#ffffff;
  --line:#e2e2e2;
}
*{box-sizing:border-box;margin:0;padding:0}
html,body{width:794px;height:1200px;overflow:hidden;background:var(--white)}
body{font-family:"Open Sans",Arial,sans-serif;color:var(--ink)}
.page{position:relative;width:794px;height:1200px}
.abs{position:absolute}

/* hero */
.hero{left:0;top:0;width:794px;height:308px;background:linear-gradient(180deg,#1f7f1f 0%,#3ea83a 45%,#8ee08a 70%,#1d4a1d 100%)}
.hero-shade{left:0;top:0;width:794px;height:308px;background:
  linear-gradient(0deg,rgba(10,40,10,.85) 0%,rgba(20,70,20,.55) 22%,rgba(0,0,0,0) 42%),
  radial-gradient(ellipse at 28% 45%,rgba(120,150,170,.55) 0%,rgba(120,150,170,0) 30%)}
.brand{left:356px;top:72px;display:flex;align-items:center;gap:9px;color:var(--white);font-size:18px;font-weight:400}
.brand-mark{width:20px;height:20px;border:2px solid var(--white);border-radius:50%}
.hero-title{left:355px;top:112px;color:var(--white);font-size:26px;line-height:32px}
.hero-title strong{font-weight:700;display:block}
.hero-title span{font-weight:300;display:block}
.btn-orange{background:linear-gradient(180deg,var(--orange-light),var(--orange));color:var(--white);font-weight:700;font-size:10px;border:1px solid #e0561a;border-radius:2px;display:flex;align-items:center;justify-content:center}
.hero-btn{left:356px;top:192px;width:86px;height:28px}

/* features */
.feature{top:330px;width:220px;text-align:center}
.feature svg{display:block;margin:0 auto;height:40px}
.feature h3{font-weight:400;font-size:15.5px;margin-top:14px;color:var(--ink);white-space:nowrap}
.feature p{font-size:8.5px;line-height:13px;color:var(--muted);margin:12px auto 0;width:176px}
.btn-green{display:flex;align-items:center;justify-content:center;width:68px;height:24px;margin:13px auto 0;background:linear-gradient(180deg,#74c766,var(--green));border:1px solid var(--green-dark);border-radius:2px;color:var(--white);font-size:9px;font-weight:600}
.divider{top:336px;width:1px;height:150px;background:var(--line)}

/* about */
.about{left:0;top:506px;width:794px;height:196px;background:var(--soft-bg)}
.about-title{left:102px;top:522px;font-weight:400;font-size:17.5px;color:var(--ink);white-space:nowrap}
.about-title em{font-style:normal;color:var(--green)}
.about-text{left:106px;top:556px;width:290px;font-size:8.5px;line-height:13px;color:var(--muted)}
.about-list{left:106px;top:611px;list-style:none;font-size:8.5px;color:var(--muted)}
.about-list li{position:relative;padding-left:12px;height:18.5px}
.about-list li::before{content:"";position:absolute;left:1px;top:3px;border-left:4px solid var(--green);border-top:3px solid transparent;border-bottom:3px solid transparent}
.video{left:406px;top:526px;width:284px;height:156px;background:linear-gradient(160deg,#2a4f8f 0%,#4d7fc2 35%,#7aa8d8 55%,#1a2f5c 100%);overflow:hidden}
.video-bar{position:absolute;left:0;bottom:0;width:284px;height:28px;background:linear-gradient(180deg,#2d2d2d,#111)}
.video-progress{position:absolute;left:0;bottom:26px;width:284px;height:4px;background:#555}
.video-progress::before{content:"";position:absolute;left:0;top:0;width:66px;height:4px;background:#cc1f1f}
.video-time{position:absolute;left:82px;bottom:8px;color:var(--white);font-size:8px;font-weight:600}
.video-quality{position:absolute;left:182px;bottom:8px;color:#bbb;font-size:8px;font-weight:700}

/* cities */
.cities-title{left:0;top:719px;width:794px;text-align:center;font-weight:400;font-size:15px;color:var(--ink)}
.city{top:750px;width:186px}
.city-photo{width:186px;height:135px;border-radius:5px;background:linear-gradient(180deg,#1b1d24 0%,#4a4236 55%,#a98a55 80%,#2a241c 100%)}
.city-name{text-align:center;font-size:11.5px;color:var(--muted);margin-top:8px}

/* contact */
.contact{left:0;top:932px;width:794px;height:224px;background:var(--green-band)}
.contact-title{left:0;top:950px;width:794px;text-align:center;color:var(--white);font-weight:400;font-size:16px}
.contact-info{left:104px;top:996px;list-style:none;color:var(--white);font-size:8.5px}
.contact-info li{display:flex;align-items:center;gap:8px;height:20.5px}
.contact-info svg{width:7px;height:7px}
.social{left:106px;top:1064px;display:flex;gap:10px}
.social span{width:20px;height:20px;border-radius:50%;background:var(--white)}
.field{left:243px;width:190px;height:25px;background:var(--white);border:1px solid #d8d8d8;font-size:8px;color:#999;display:flex;align-items:center;justify-content:space-between;padding:0 9px 0 10px}
.field svg{width:9px;height:9px}
.message{left:440px;top:998px;width:254px;height:87px;background:var(--white);border:1px solid #d8d8d8}
.send-btn{left:608px;top:1098px;width:86px;height:27px;font-size:10px}

/* footer */
.footer-copy{left:105px;top:1171px;font-size:8.5px;color:var(--muted)}
.footer-nav{right:104px;top:1171px;display:flex;gap:18px;font-size:8.5px;color:var(--muted)}
</style>
</head>
<body>
<div class="page">

  <section class="abs hero" role="img" aria-label="Green-tinted night city skyline with a bridge and a smiling man in a shirt and tie presenting the message"></section>
  <div class="abs hero-shade" aria-hidden="true"></div>
  <div class="abs brand"><span class="brand-mark"></span>Quiet Horizon</div>
  <h1 class="abs hero-title"><strong>Reducing and eliminating</strong><span>the wasted lighting.</span></h1>
  <a class="abs btn-orange hero-btn">Contact Us</a>

  <div class="abs feature" style="left:79px">
    <svg viewBox="0 0 30 42" aria-hidden="true"><path d="M15 2a12 12 0 0 0-7 21.7c1.3 1 2 2.3 2 3.8V31h10v-3.5c0-1.5.7-2.8 2-3.8A12 12 0 0 0 15 2z" fill="var(--green)"/><path d="M15 6a8 8 0 0 0-5 14" stroke="#bfe6b8" stroke-width="2" fill="none"/><rect x="10" y="33" width="10" height="3" rx="1" fill="var(--green)"/><rect x="11.5" y="37.5" width="7" height="3" rx="1.5" fill="var(--green)"/></svg>
    <h3>Our Lighting Expertise</h3>
    <p>Lorem ipsum dolor sit amet, pro aeterno adipisci ex, pro no iriure accusam. Eros admodum intellegat ex mea,</p>
    <a class="btn-green">Read More</a>
  </div>
  <div class="abs divider" style="left:287px"></div>
  <div class="abs feature" style="left:278px">
    <svg viewBox="0 0 52 42" aria-hidden="true"><ellipse cx="33" cy="14" rx="18" ry="12" fill="var(--green)"/><path d="M42 24l6 8-11-5z" fill="var(--green)"/><ellipse cx="18" cy="22" rx="16" ry="11" fill="#4a9c3f"/><path d="M8 30l-6 9 12-5z" fill="#4a9c3f"/></svg>
    <h3>Our Customer Centricity</h3>
    <p>Lorem ipsum dolor sit amet, pro aeterno adipisci ex, pro no iriure accusam. Eros admodum intellegat ex mea,</p>
    <a class="btn-green">Read More</a>
  </div>
  <div class="abs divider" style="left:487px"></div>
  <div class="abs feature" style="left:478px">
    <svg viewBox="0 0 40 42" aria-hidden="true"><path d="M6 24v-6a14 14 0 0 1 28 0v6" stroke="var(--green)" stroke-width="4" fill="none"/><rect x="2" y="20" width="8" height="14" rx="3" fill="var(--green)"/><rect x="30" y="20" width="8" height="14" rx="3" fill="var(--green)"/><path d="M34 34c0 4-5 6-11 6" stroke="var(--green)" stroke-width="3" fill="none"/><circle cx="21" cy="40" r="2.5" fill="var(--green)"/></svg>
    <h3>Our Compliance Assistance</h3>
    <p>Lorem ipsum dolor sit amet, pro aeterno adipisci ex, pro no iriure accusam. Eros admodum intellegat ex mea,</p>
    <a class="btn-green">Read More</a>
  </div>

  <section class="abs about"></section>
  <h2 class="abs about-title">What is this <em>Quiet Horizon</em> all about?</h2>
  <p class="abs about-text">Lorem ipsum dolor sit amet, pro aeterno adipisci ex, pro no iriure accusam. Eros admodum intellegat ex mea, mei wisi nullam ne, qui cu aliquid nominavi.</p>
  <ul class="abs about-list">
    <li>Lorem ipsum dolor sit amet, pro aeterno adipisci ex</li>
    <li>Peros admodum intellegat ex mea</li>
    <li>Ivim quod elitr interesset ea lore ipsum dolor vimos</li>
    <li>Lorem ipsum dolor sit amet, pro aeterno adipisci ex</li>
  </ul>
  <div class="abs video" role="img" aria-label="Video player showing glass office towers at dusk with lit windows">
    <div class="video-progress"></div>
    <div class="video-bar">
      <svg style="position:absolute;left:22px;top:8px" width="10" height="12" viewBox="0 0 10 12" aria-hidden="true"><path d="M0 0l10 6-10 6z" fill="#ccc"/></svg>
      <svg style="position:absolute;left:55px;top:8px" width="14" height="12" viewBox="0 0 14 12" aria-hidden="true"><path d="M0 4h3l4-4v12l-4-4H0z" fill="#ccc"/><path d="M9 3a4 4 0 0 1 0 6M11 1a7 7 0 0 1 0 10" stroke="#ccc" fill="none"/></svg>
      <span class="video-time">0:00 / 4:37</span>
      <span class="video-quality">720p</span>
      <svg style="position:absolute;left:216px;top:8px" width="60" height="12" viewBox="0 0 60 12" aria-hidden="true"><rect x="0" y="3" width="12" height="7" fill="#bbb"/><rect x="20" y="1" width="17" height="10" fill="#bbb"/><rect x="45" y="0" width="15" height="12" fill="none" stroke="#bbb" stroke-width="2"/></svg>
    </div>
  </div>

  <h2 class="abs cities-title">Sample Cities/Areas</h2>
  <div class="abs city" style="left:106px"><div class="city-photo" role="img" aria-label="New York skyline at night with lit office windows"></div><p class="city-name">New York</p></div>
  <div class="abs city" style="left:307px"><div class="city-photo" role="img" aria-label="San Francisco skyline at night with lit office windows"></div><p class="city-name">San Francisco</p></div>
  <div class="abs city" style="left:504px"><div class="city-photo" role="img" aria-label="Los Angeles skyline at night with lit office windows"></div><p class="city-name">Los Angeles</p></div>

  <section class="abs contact"></section>
  <h2 class="abs contact-title">Contact us now and start reducing the wasted lighting.</h2>
  <ul class="abs contact-info">
    <li><svg viewBox="0 0 8 8" aria-hidden="true"><path d="M4 0a3 3 0 0 0-3 3c0 2 3 5 3 5s3-3 3-5a3 3 0 0 0-3-3z" fill="#fff"/></svg>Lantern Street No: 8/12</li>
    <li><svg viewBox="0 0 8 8" aria-hidden="true"><path d="M0 2c0-1 1-2 4-2s4 1 4 2v1H6V2H2v1H0zM1 4h6v4H1z" fill="#fff"/></svg>0312 608 44 19</li>
    <li><svg viewBox="0 0 8 8" aria-hidden="true"><rect x="0" y="1" width="8" height="6" fill="#fff"/><path d="M0 1l4 3 4-3" stroke="#6dbd63" fill="none"/></svg>hello@quiethorizon.example</li>
  </ul>
  <div class="abs social" aria-label="Social links"><span></span><span></span><span></span><span></span></div>

  <div class="abs field" style="top:998px">Your Name<svg viewBox="0 0 9 9" aria-hidden="true"><circle cx="4.5" cy="2.5" r="2.3" fill="#bbb"/><path d="M0 9a4.5 4 0 0 1 9 0z" fill="#bbb"/></svg></div>
  <div class="abs field" style="top:1029px">Email<svg viewBox="0 0 9 9" aria-hidden="true"><rect y="1.5" width="9" height="6" fill="#bbb"/><path d="M0 1.5l4.5 3.5 4.5-3.5" stroke="#fff" fill="none"/></svg></div>
  <div class="abs field" style="top:1060px">Subject<svg viewBox="0 0 9 9" aria-hidden="true"><ellipse cx="5.5" cy="3.5" rx="3.5" ry="2.5" fill="#bbb"/><ellipse cx="3" cy="5.5" rx="3" ry="2.2" fill="#ccc"/></svg></div>
  <div class="abs message" aria-label="Message"></div>
  <a class="abs btn-orange send-btn">Send Message</a>

  <p class="abs footer-copy">Copyright © 2014- Company Name</p>
  <nav class="abs footer-nav"><a>Contact</a><a>Support</a><a>Privacy Policy</a></nav>
</div>
</body>
</html>
```